Business card n Letter heads for an IT Company
Quorvane Systems JLT
Business card n Letter heads for an IT Company - Information Technology
Creative Brief
Bright & Fun-filled
Rohan Mextapur
Sales Manager
2817,Halvering Business Tower, Pelmar D, Dubai UAE
rohan@quorvane.com
www.quorvane.com
An Dravolk Group Company

```html
<!DOCTYPE html>
<html lang="en">
<head>
<meta charset="utf-8">
<title>Quorvane Systems JLT — Business Card</title>
<link rel="stylesheet" href="https://fonts.googleapis.com/css2?family=Ubuntu:wght@400;500;700&display=swap">
<style>
  :root {
    --backdrop: #9a9c9e;
    --card-white: #ffffff;
    --brand-red: #c00d0d;
    --brand-yellow: #f6b814;
    --ink-grey: #5e5e5e;
    --rule-grey: #9c9c9c;
  }
  * { box-sizing: border-box; margin: 0; padding: 0; }
  html, body { width: 1200px; height: 895px; overflow: hidden; }
  body {
    background: var(--backdrop);
    font-family: "Ubuntu", sans-serif;
    position: relative;
  }
  .card {
    position: absolute;
    width: 520px;
    height: 297px;
    box-shadow: 0 6px 18px rgba(0,0,0,0.28);
  }
  .card-front { left: 60px; top: 330px; background: var(--card-white); }
  .card-back { left: 620px; top: 330px; background: var(--brand-red); }

  .logo {
    position: absolute;
    left: 150px; top: 70px;
    display: flex; align-items: center; gap: 10px;
  }
  .logo-square {
    width: 30px; height: 30px; border-radius: 5px;
    background: var(--brand-yellow);
  }
  .logo-name {
    font-size: 52px; font-weight: 500; letter-spacing: -1px;
    color: var(--brand-red); line-height: 1;
  }

  .person {
    position: absolute; left: 0; right: 0; top: 160px;
    text-align: center;
    font-size: 12px; letter-spacing: 1.2px;
    font-variant: small-caps;
    color: var(--brand-red);
  }
  .person .divider { color: var(--rule-grey); margin: 0 8px; }
  .person .role { color: var(--ink-grey); }

  .contacts {
    position: absolute; left: 40px; right: 30px; top: 205px;
    display: grid; grid-template-columns: 1.6fr 1fr;
    row-gap: 9px; column-gap: 20px;
    font-size: 9px; letter-spacing: 0.6px;
    font-variant: small-caps;
    color: var(--ink-grey);
  }
  .contact { display: flex; align-items: center; gap: 7px; white-space: nowrap; }
  .contact svg { width: 11px; height: 11px; flex: none; }

  .web-address {
    position: absolute; right: 36px; top: 192px;
    font-size: 15px; letter-spacing: 5px;
    color: var(--card-white);
  }
</style>
</head>
<body>
  <section class="card card-front" aria-label="Business card front">
    <div class="logo">
      <span class="logo-square"></span>
      <span class="logo-name">quorvane</span>
    </div>

    <p class="person">
      <span class="name">Rohan Mextapur</span><span class="divider">/</span><span class="role">Sales Manager</span>
    </p>

    <div class="contacts">
      <div class="contact">
        <svg viewBox="0 0 12 12"><circle cx="6" cy="6" r="6" fill="var(--brand-red)"/><path d="M6 2.6a2 2 0 0 1 2 2c0 1.5-2 4-2 4s-2-2.5-2-4a2 2 0 0 1 2-2z" fill="#fff"/></svg>
        <span>2817,Halvering Business Tower, Pelmar D, Dubai UAE</span>
      </div>
      <div class="contact">
        <svg viewBox="0 0 12 12"><circle cx="6" cy="6" r="6" fill="var(--brand-red)"/><circle cx="6" cy="6" r="3" fill="none" stroke="#fff" stroke-width="0.9"/><line x1="3" y1="6" x2="9" y2="6" stroke="#fff" stroke-width="0.8"/></svg>
        <span>www.quorvane.com</span>
      </div>
      <div class="contact">
        <svg viewBox="0 0 12 12"><circle cx="6" cy="6" r="6" fill="var(--brand-red)"/><path d="M3.5 4.2c0 2.4 1.9 4.3 4.3 4.3l0.8-1-1.2-0.8-0.6 0.6c-0.8-0.4-1.4-1-1.8-1.8l0.6-0.6-0.8-1.2z" fill="#fff"/></svg>
        <span>+971 4 555 0141</span>
      </div>
      <div class="contact">
        <svg viewBox="0 0 12 12"><circle cx="6" cy="6" r="6" fill="var(--brand-red)"/><rect x="3" y="4" width="6" height="4" fill="none" stroke="#fff" stroke-width="0.8"/><path d="M3 4l3 2.2L9 4" fill="none" stroke="#fff" stroke-width="0.8"/></svg>
        <span>rohan@quorvane.com</span>
      </div>
      <div class="contact">
        <svg viewBox="0 0 12 12"><circle cx="6" cy="6" r="6" fill="var(--brand-red)"/><rect x="4.3" y="2.8" width="3.4" height="6.4" rx="0.6" fill="none" stroke="#fff" stroke-width="0.8"/></svg>
        <span>+971 50 555 0192</span>
      </div>
      <div class="contact">
        <svg viewBox="0 0 12 12"><circle cx="6" cy="6" r="6" fill="var(--brand-red)"/><rect x="3.2" y="5" width="5.6" height="3.4" fill="#fff"/><rect x="4.2" y="3.2" width="3.6" height="1.8" fill="none" stroke="#fff" stroke-width="0.7"/></svg>
        <span>+971 4 555 0142</span>
      </div>
    </div>
  </section>

  <section class="card card-back" aria-label="Business card back">
    <p class="web-address">WWW.QUORVANE.COM</p>
  </section>
</body>
</html>
```